New Flyer Design Project*

The business provides eyelash extensions and hair services. Mostly eyelash extension photos and reviews are seen, so please visit www.mirelbeauty.com for more information!

My target audience consists of women aged 18-50 (quite broad) but all demographics is fine. The store is in Lakeway, TX, so while the majority is Caucasian, a lot of diverse customers come in as well!

In terms of ideas, I want a modern approach that is pretty minimal but also depicts examples of eyelash extensions for people to get a visual aid. I like black, gray, white, gold, brown, and green, so a good balance of those would be really nice. I also like to make it really easy to read so that people of older age wouldn't struggle reading it! I would also like a title page, menu, brief history of my services, and referral/contact info on the back.

Colors

Designer to choose colors to be used in the design.

Requirements
Must have
• https://www.ratespot.com/biz/mirel-beauty-lakeway

```html
<!DOCTYPE html>
<html lang="en">
<head>
<meta charset="utf-8">
<title>Mirel Beauty – Brochure Outside</title>
<link href="https://fonts.googleapis.com/css2?family=Cinzel:wght@400;600&family=Montserrat:wght@400;500;600&display=swap" rel="stylesheet">
<style>
  :root{
    --backdrop:#262626;
    --paper:#f7f7f7;
    --paper-shade:#ececec;
    --gold:#c8913a;
    --gold-deep:#a8722a;
    --gold-light:#ddb06a;
    --ink:#2e2e2e;
    --muted:#8a8a8a;
    --silver:#e4e4e4;
    --white:#ffffff;
  }
  *{margin:0;padding:0;box-sizing:border-box}
  html,body{width:867px;height:1200px;overflow:hidden;background:var(--backdrop)}
  .canvas{position:relative;width:867px;height:1200px}
  .brochure{position:absolute;left:0;top:293px;width:867px;height:614px;
    background:linear-gradient(90deg,var(--paper) 0%,var(--white) 50%,var(--paper) 100%);
    overflow:hidden;font-family:"Montserrat",sans-serif;color:var(--ink)}
  .fold{position:absolute;left:433px;top:0;width:1px;height:614px;background:rgba(0,0,0,.06)}
  .wave{position:absolute;left:0;top:0}
  .abs{position:absolute}

  /* left panel */
  .about-title{left:25px;top:31px;font-family:"Cinzel",serif;font-weight:600;font-size:15px;letter-spacing:.3px}
  .about-title .brand{color:var(--gold)}
  .about-copy{left:25px;width:388px;font-size:8.6px;line-height:12.4px}
  .about-copy .brand{color:var(--gold-deep);font-weight:600}
  .quote-mark{font-family:"Cinzel",serif;font-weight:600;font-size:40px;line-height:30px;color:var(--gold)}
  .quote-frame{left:37px;width:382px;border-left:1px solid #c9c9c9;border-bottom:1px solid #c9c9c9}
  .quote-text{left:52px;width:340px;font-size:8.6px;line-height:12px}
  .quote-name{font-size:8.6px;font-weight:600;color:var(--gold-deep)}
  .map{left:23px;top:411px;width:132px;height:132px;border-radius:50%;
    background:radial-gradient(circle at 45% 45%,#f3f3f3,#dcdcdc);border:5px solid var(--white);
    box-shadow:0 2px 6px rgba(0,0,0,.25)}
  .contact-title{left:162px;top:535px;width:140px;text-align:center;font-family:"Cinzel",serif;
    font-weight:600;font-size:11px;color:var(--white);border-bottom:1px solid rgba(255,255,255,.6);padding-bottom:4px}
  .contact-row{top:569px;font-size:10px;line-height:12.5px;color:var(--white);display:flex;gap:5px;align-items:flex-start}
  .sep{top:568px;width:1px;height:18px;background:rgba(255,255,255,.55)}

  /* right panel */
  .portrait{left:600px;top:0;width:267px;height:430px;
    background:radial-gradient(ellipse at 65% 45%,#f2d9c8 0%,#e6c2ab 45%,rgba(240,230,222,0) 75%)}
  .logo-ring{left:505px;top:44px;width:70px;height:70px;border-radius:50%;border:2px solid var(--gold)}
  .logo-name{left:433px;width:212px;top:124px;text-align:center;font-family:"Cinzel",serif;
    font-size:21px;color:var(--gold);letter-spacing:1px}
  .logo-rule{left:465px;top:156px;width:148px;height:1px;background:var(--gold)}
  .photo{border-radius:50%;border:5px solid var(--white);box-shadow:0 2px 7px rgba(0,0,0,.25)}
  .photo-a{left:456px;top:384px;width:104px;height:104px;background:radial-gradient(circle at 45% 40%,#c99a80,#5b4536)}
  .photo-b{left:580px;top:345px;width:114px;height:114px;background:radial-gradient(circle at 50% 40%,#e3bea5,#9a7a68)}
  .photo-c{left:716px;top:353px;width:124px;height:124px;background:radial-gradient(circle at 45% 50%,#7a5a4a,#e9d2c4 60%)}
  .welcome{left:433px;width:434px;text-align:center;color:var(--white);font-family:"Cinzel",serif}
  .welcome-small{top:476px;font-size:18px;letter-spacing:.5px}
  .welcome-big{top:494px;font-size:36px;letter-spacing:1px}
  .tagline{left:433px;width:434px;top:553px;text-align:center;font-size:10.5px;color:var(--white)}
  .site{left:433px;width:434px;top:583px;text-align:center;font-size:9.5px;letter-spacing:3px;color:var(--white)}
</style>
</head>
<body>
<div class="canvas">
  <section class="brochure">
    <svg class="wave" width="867" height="614" viewBox="0 0 867 614" aria-hidden="true">
      <defs>
        <linearGradient id="goldFill" x1="0" y1="0" x2="1" y2="1">
          <stop offset="0" stop-color="#d6a24e"/>
          <stop offset=".5" stop-color="#c8913a"/>
          <stop offset="1" stop-color="#b37c2e"/>
        </linearGradient>
      </defs>
      <path d="M0,505 C140,520 300,480 433,452 C580,420 720,395 867,405 L867,614 L0,614 Z" fill="#e8e8e8"/>
      <path d="M0,515 C140,528 300,490 433,462 C580,430 720,406 867,414 L867,614 L0,614 Z" fill="url(#goldFill)"/>
      <path d="M0,560 C200,540 360,590 433,614 L0,614 Z" fill="#d9a859" opacity=".35"/>
    </svg>
    <div class="fold"></div>

    <!-- left panel -->
    <h2 class="abs about-title">What is <span class="brand">Mirel Beauty?</span></h2>
    <p class="abs about-copy" style="top:58px">It's always been much more than the typical hair salon as Mirel Beauty strives to reach perfection for everything we do. We feature highly trained professionals whose dedication exceeds all others, and our results prove that looking the best you can be can be found easily. Our range of services puts us greatly ahead. Each service is done to its fullest and we make sure that every client is more than satisfied when they enter, as well as when they leave.</p>
    <p class="abs about-copy" style="top:143px">To us, Mirel Beauty is the want to excel, the need to perform at the highest level, and to treat everyone as if they were royalty.</p>
    <p class="abs about-copy" style="top:178px">Welcome to <span class="brand">Mirel Beauty Lash Studio</span> and may your experience be unparalleled.</p>

    <div class="abs quote-frame" style="top:229px;height:53px"></div>
    <div class="abs quote-mark" style="left:53px;top:214px">“</div>
    <p class="abs quote-text" style="top:249px">Its been a year since I've been seeing Delia and I cant stop seeing her! Her work is AMAZING! Im so glad I went with her a year ago!!! She is the best!!!</p>
    <div class="abs quote-name" style="left:376px;top:276px">Renata P.</div>

    <div class="abs quote-frame" style="top:305px;height:70px"></div>
    <div class="abs quote-mark" style="left:53px;top:290px">“</div>
    <p class="abs quote-text" style="top:324px">Delia does an outstanding job! My lashes last for a 5 weeks and feel so light and natural. I drive all the way from San Francisco to have my lashes done! Her schedule gets super busy but that's because she does an amazing job so make sure you book in advance. Highly recommend</p>
    <div class="abs quote-name" style="left:340px;top:369px">Corinne L.</div>

    <div class="abs map" role="img" aria-label="Street map showing the studio location in Lakeway"></div>
    <div class="abs contact-title">Contact Us Today</div>

    <div class="abs contact-row" style="left:20px">
      <svg width="10" height="12" viewBox="0 0 10 12" aria-hidden="true"><path d="M5 1a3.5 3.5 0 0 0-3.5 3.5C1.5 7.5 5 11 5 11s3.5-3.5 3.5-6.5A3.5 3.5 0 0 0 5 1z" fill="none" stroke="#fff" stroke-width="1"/><circle cx="5" cy="4.5" r="1.2" fill="#fff"/></svg>
      <span>482 Lakeview Trail,<br>Lakeway, TX 78734</span>
    </div>
    <div class="abs sep" style="left:165px"></div>
    <div class="abs contact-row" style="left:180px">
      <svg width="11" height="11" viewBox="0 0 11 11" aria-hidden="true"><path d="M2.2 1h2l1 2.5-1.3 1a6 6 0 0 0 2.6 2.6l1-1.3L10 6.8v2A1.2 1.2 0 0 1 8.8 10 8 8 0 0 1 1 2.2 1.2 1.2 0 0 1 2.2 1z" fill="none" stroke="#fff" stroke-width="1"/></svg>
      <span>(512) 555-0148</span>
    </div>
    <div class="abs sep" style="left:282px"></div>
    <div class="abs contact-row" style="left:294px">
      <svg width="11" height="11" viewBox="0 0 11 11" aria-hidden="true"><circle cx="5.5" cy="5.5" r="4.5" fill="none" stroke="#fff"/><ellipse cx="5.5" cy="5.5" rx="2" ry="4.5" fill="none" stroke="#fff"/><path d="M1 5.5h9" stroke="#fff"/></svg>
      <span>www.mirelbeauty.com</span>
    </div>

    <!-- right panel -->
    <div class="abs portrait" role="img" aria-label="Close-up portrait of a model wearing eyelash extensions"></div>
    <div class="abs logo-ring" aria-hidden="true"></div>
    <div class="abs logo-name">Mirel Beauty</div>
    <div class="abs logo-rule"></div>

    <div class="abs photo photo-a" role="img" aria-label="Client showing finished lash extensions"></div>
    <div class="abs photo photo-b" role="img" aria-label="Lash artist at the studio"></div>
    <div class="abs photo photo-c" role="img" aria-label="Close-up of an eye with lash extensions"></div>

    <div class="abs welcome welcome-small">Welcome to</div>
    <div class="abs welcome welcome-big">Mirel Beauty</div>
    <div class="abs tagline">Get Ready To Bat Those Eyelashes With Confidence!</div>
    <div class="abs site">www.mirelbeauty.com</div>
  </section>
</div>
</body>
</html>
```